Business card design needed

Just need something dynamic and unique
For a local painting contractor

Industry/Entity Type

Painting

Contact Information for Business Card

Warren Pike
Painting Contactor
Interior & Exterior
New Work & Repaints
For an obligation free quote:
0437516082

```html
<!DOCTYPE html>
<html lang="en">
<head>
<meta charset="utf-8">
<title>Warren Pike Painting Contactor – Business Card</title>
<link rel="stylesheet" href="https://fonts.googleapis.com/css2?family=Oswald:wght@500&family=Mulish:ital,wght@1,400&family=Didact+Gothic&display=swap">
<style>
  :root {
    --page: #ffffff;
    --ink: #111111;
    --red: #d4301f;
    --orange: #ee6a1c;
    --amber: #f5a81c;
    --yellow: #f3d93c;
    --lime: #9cc43c;
    --green: #1c8a3c;
    --band: rgba(255, 255, 255, 0.94);
    --quote-brown: #9a4a1f;
    --quote-gold: #c98f1a;
    --quote-olive: #a9a22a;
    --quote-green: #4b9a3a;
  }
  html, body {
    margin: 0;
    width: 1200px;
    height: 900px;
    overflow: hidden;
    background: var(--page);
  }
  .business-card {
    position: absolute;
    left: 56px;
    top: 114px;
    width: 1088px;
    height: 672px;
    overflow: hidden;
  }
  .card-backdrop {
    position: absolute;
    inset: 0;
    background:
      radial-gradient(ellipse 40% 45% at 55% 42%, rgba(255, 240, 150, 0.85), rgba(255, 240, 150, 0) 70%),
      radial-gradient(ellipse 35% 40% at 95% 95%, rgba(20, 130, 60, 0.9), rgba(20, 130, 60, 0) 80%),
      linear-gradient(100deg, var(--red) 0%, var(--orange) 24%, var(--amber) 46%, var(--yellow) 60%, var(--lime) 76%, var(--green) 100%);
  }
  .business-name {
    position: absolute;
    right: 48px;
    top: 272px;
    margin: 0;
    font-family: "Oswald", sans-serif;
    font-weight: 500;
    font-size: 64px;
    line-height: 1;
    color: var(--ink);
    white-space: nowrap;
  }
  .services {
    position: absolute;
    right: 48px;
    top: 342px;
    margin: 0;
    font-family: "Oswald", sans-serif;
    font-weight: 500;
    font-size: 40px;
    letter-spacing: 2px;
    line-height: 1;
    color: var(--ink);
  }
  .tagline {
    position: absolute;
    right: 48px;
    top: 420px;
    margin: 0;
    font-family: "Mulish", sans-serif;
    font-style: italic;
    font-size: 37px;
    line-height: 1;
    color: var(--ink);
    white-space: nowrap;
  }
  .quote-band {
    position: absolute;
    left: 0;
    right: 0;
    top: 512px;
    height: 78px;
    background: var(--band);
    display: flex;
    align-items: center;
  }
  .quote-line {
    margin: 0 0 0 80px;
    font-family: "Didact Gothic", sans-serif;
    font-size: 50px;
    line-height: 1;
    white-space: nowrap;
  }
  .quote-line .c1 { color: var(--quote-brown); }
  .quote-line .c2 { color: var(--quote-gold); }
  .quote-line .c3 { color: var(--quote-olive); }
  .quote-line .c4 { color: var(--quote-green); }
</style>
</head>
<body>
  <div class="business-card">
    <div class="card-backdrop" role="img" aria-label="Abstract background of crossing light streaks in red, orange, yellow and green"></div>
    <h1 class="business-name">Warren Pike Painting Contactor</h1>
    <p class="services">Interior Exterior</p>
    <p class="tagline">New Work Repaints For an obligation</p>
    <div class="quote-band">
      <p class="quote-line"><span class="c1">Call for a</span> <span class="c2">free quote:</span> <span class="c3">0437</span><span class="c4">516082</span></p>
    </div>
  </div>
</body>
</html>
```